Bref créative
Tamsel Briar Gifts
making every gift "one of a kind!"
Bright & Fun-filled
Marta Fowler
Owner
no address - online only
fowler@tamselbriargifts.example
www.tamselbriargifts.example
I would like my logo on the front in white background.
I would like my logo in black background.

```html
<!DOCTYPE html>
<html lang="en">
<head>
<meta charset="utf-8">
<title>Tamsel Briar Gifts – Business Card Options</title>
<link rel="stylesheet" href="https://fonts.googleapis.com/css2?family=Open+Sans:ital,wght@0,400;0,600;1,400&display=swap">
<style>
  :root {
    --board: #4a4a4a;
    --card: #ffffff;
    --magenta: #a3277a;
    --magenta-deep: #8a1d66;
    --gold: #b08a3c;
    --ink: #3d3d3d;
    --muted: #7a7a7a;
    --caption: #b9b9b9;
  }
  * { box-sizing: border-box; margin: 0; padding: 0; }
  html, body { width: 1200px; height: 655px; overflow: hidden; }
  body {
    background: radial-gradient(ellipse at center, #555 0%, var(--board) 70%, #3e3e3e 100%);
    font-family: "Open Sans", Arial, sans-serif;
    position: relative;
  }
  .option {
    position: absolute;
    width: 293px;
  }
  .card {
    position: relative;
    width: 293px;
    height: 170px;
    background: var(--card);
    border-radius: 9px;
    overflow: hidden;
    box-shadow: 0 3px 8px rgba(0,0,0,.45);
  }
  .brand {
    position: absolute;
    top: 24px; left: 0; right: 0;
    text-align: center;
  }
  .brand-name {
    font-size: 19px;
    font-weight: 400;
    color: var(--magenta);
    letter-spacing: .2px;
  }
  .tagline {
    margin-top: 3px;
    font-size: 6.5px;
    font-style: italic;
    color: var(--muted);
  }
  .person {
    position: absolute;
    top: 86px; left: 20px;
    width: 98px;
    text-align: right;
  }
  .person-name { font-size: 9.5px; font-weight: 600; color: var(--gold); }
  .person-role { font-size: 6px; color: var(--muted); margin-top: 3px; }
  .divider {
    position: absolute;
    top: 82px; left: 128px;
    width: 1px; height: 38px;
    background: #cfcfcf;
  }
  .contacts {
    position: absolute;
    top: 82px; left: 138px;
    list-style: none;
  }
  .contacts li {
    display: flex; align-items: center;
    font-size: 6px; color: var(--ink);
    height: 12px;
  }
  .contacts svg { width: 7px; height: 7px; margin-right: 5px; fill: var(--ink); }
  .swoosh { position: absolute; left: 0; bottom: 0; width: 293px; height: 170px; }
  .caption {
    margin-top: 14px;
    text-align: center;
    font-size: 8px;
    color: var(--caption);
  }
  .col-1 { left: 103px; } .col-2 { left: 466px; } .col-3 { left: 826px; }
  .row-1 { top: 113px; } .row-2 { top: 360px; }
</style>
</head>
<body>
<main class="board">

  <!-- reusable card body repeated per option -->
  <section class="option col-1 row-1">
    <div class="card">
      <svg class="swoosh" viewBox="0 0 293 170"><path d="M0,150 Q150,172 293,122 L293,170 L0,170Z" fill="var(--magenta)"/><path d="M0,141 Q145,162 293,116" stroke="var(--gold)" stroke-width="2" fill="none"/></svg>
      <div class="brand"><div class="brand-name">Tamsel Briar Gifts</div><div class="tagline">making every gift "one of a kind!"</div></div>
      <div class="person"><div class="person-name">Marta Fowler</div><div class="person-role">Owner</div></div>
      <div class="divider"></div>
      <ul class="contacts">
        <li><svg viewBox="0 0 10 10"><path d="M2,0 L4,2 L3,4 Q4,6 6,7 L8,6 L10,8 L8,10 Q0,9 0,2Z"/></svg>555-014-2288</li>
        <li><svg viewBox="0 0 10 10"><path d="M0,2 H10 V8 H0Z M0,2 L5,6 L10,2" fill="none" stroke="var(--ink)"/></svg>fowler@tamselbriargifts.example</li>
        <li><svg viewBox="0 0 10 10"><circle cx="5" cy="5" r="4.5"/></svg>www.tamselbriargifts.example</li>
      </ul>
    </div>
    <p class="caption">Front Card Option_01</p>
  </section>

  <section class="option col-2 row-1">
    <div class="card">
      <svg class="swoosh" viewBox="0 0 293 170"><path d="M0,140 Q120,170 293,150 L293,170 L0,170Z" fill="var(--magenta)"/><path d="M0,132 Q125,162 293,142" stroke="var(--gold)" stroke-width="2" fill="none"/></svg>
      <div class="brand"><div class="brand-name">Tamsel Briar Gifts</div><div class="tagline">making every gift "one of a kind!"</div></div>
      <div class="person"><div class="person-name">Marta Fowler</div><div class="person-role">Owner</div></div>
      <div class="divider"></div>
      <ul class="contacts">
        <li><svg viewBox="0 0 10 10"><path d="M2,0 L4,2 L3,4 Q4,6 6,7 L8,6 L10,8 L8,10 Q0,9 0,2Z"/></svg>555-014-2288</li>
        <li><svg viewBox="0 0 10 10"><path d="M0,2 H10 V8 H0Z M0,2 L5,6 L10,2" fill="none" stroke="var(--ink)"/></svg>fowler@tamselbriargifts.example</li>
        <li><svg viewBox="0 0 10 10"><circle cx="5" cy="5" r="4.5"/></svg>www.tamselbriargifts.example</li>
      </ul>
    </div>
    <p class="caption">Front Card Option_02</p>
  </section>

  <section class="option col-3 row-1">
    <div class="card">
      <svg class="swoosh" viewBox="0 0 293 170"><path d="M0,128 Q150,175 293,152 L293,170 L0,170Z" fill="var(--magenta)"/><path d="M0,122 Q150,166 293,146" stroke="var(--gold)" stroke-width="2" fill="none"/></svg>
      <div class="brand"><div class="brand-name">Tamsel Briar Gifts</div><div class="tagline">making every gift "one of a kind!"</div></div>
      <div class="person"><div class="person-name">Marta Fowler</div><div class="person-role">Owner</div></div>
      <div class="divider"></div>
      <ul class="contacts">
        <li><svg viewBox="0 0 10 10"><path d="M2,0 L4,2 L3,4 Q4,6 6,7 L8,6 L10,8 L8,10 Q0,9 0,2Z"/></svg>555-014-2288</li>
        <li><svg viewBox="0 0 10 10"><path d="M0,2 H10 V8 H0Z M0,2 L5,6 L10,2" fill="none" stroke="var(--ink)"/></svg>fowler@tamselbriargifts.example</li>
        <li><svg viewBox="0 0 10 10"><circle cx="5" cy="5" r="4.5"/></svg>www.tamselbriargifts.example</li>
      </ul>
    </div>
    <p class="caption">Front Card Option_03</p>
  </section>

  <section class="option col-1 row-2">
    <div class="card">
      <svg class="swoosh" viewBox="0 0 293 170"><path d="M0,150 Q150,172 293,122 L293,170 L0,170Z" fill="var(--magenta-deep)"/><path d="M0,141 Q145,162 293,116" stroke="var(--gold)" stroke-width="2" fill="none"/></svg>
      <div class="brand"><div class="brand-name">Tamsel Briar Gifts</div><div class="tagline">making every gift "one of a kind!"</div></div>
      <div class="person"><div class="person-name">Marta Fowler</div><div class="person-role">Owner</div></div>
      <div class="divider"></div>
      <ul class="contacts">
        <li><svg viewBox="0 0 10 10"><path d="M2,0 L4,2 L3,4 Q4,6 6,7 L8,6 L10,8 L8,10 Q0,9 0,2Z"/></svg>555-014-2288</li>
        <li><svg viewBox="0 0 10 10"><path d="M0,2 H10 V8 H0Z M0,2 L5,6 L10,2" fill="none" stroke="var(--ink)"/></svg>fowler@tamselbriargifts.example</li>
        <li><svg viewBox="0 0 10 10"><circle cx="5" cy="5" r="4.5"/></svg>www.tamselbriargifts.example</li>
      </ul>
    </div>
    <p class="caption">Front Card Option_04</p>
  </section>

  <section class="option col-2 row-2">
    <div class="card">
      <svg class="swoosh" viewBox="0 0 293 170"><path d="M0,140 Q120,170 293,150 L293,170 L0,170Z" fill="var(--magenta-deep)"/><path d="M0,132 Q125,162 293,142" stroke="var(--gold)" stroke-width="2" fill="none"/></svg>
      <div class="brand"><div class="brand-name">Tamsel Briar Gifts</div><div class="tagline">making every gift "one of a kind!"</div></div>
      <div class="person"><div class="person-name">Marta Fowler</div><div class="person-role">Owner</div></div>
      <div class="divider"></div>
      <ul class="contacts">
        <li><svg viewBox="0 0 10 10"><path d="M2,0 L4,2 L3,4 Q4,6 6,7 L8,6 L10,8 L8,10 Q0,9 0,2Z"/></svg>555-014-2288</li>
        <li><svg viewBox="0 0 10 10"><path d="M0,2 H10 V8 H0Z M0,2 L5,6 L10,2" fill="none" stroke="var(--ink)"/></svg>fowler@tamselbriargifts.example</li>
        <li><svg viewBox="0 0 10 10"><circle cx="5" cy="5" r="4.5"/></svg>www.tamselbriargifts.example</li>
      </ul>
    </div>
    <p class="caption">Front Card Option_05</p>
  </section>

  <section class="option col-3 row-2">
    <div class="card">
      <svg class="swoosh" viewBox="0 0 293 170"><path d="M0,128 Q150,175 293,152 L293,170 L0,170Z" fill="var(--magenta-deep)"/><path d="M0,122 Q150,166 293,146" stroke="var(--gold)" stroke-width="2" fill="none"/></svg>
      <div class="brand"><div class="brand-name">Tamsel Briar Gifts</div><div class="tagline">making every gift "one of a kind!"</div></div>
      <div class="person"><div class="person-name">Marta Fowler</div><div class="person-role">Owner</div></div>
      <div class="divider"></div>
      <ul class="contacts">
        <li><svg viewBox="0 0 10 10"><path d="M2,0 L4,2 L3,4 Q4,6 6,7 L8,6 L10,8 L8,10 Q0,9 0,2Z"/></svg>555-014-2288</li>
        <li><svg viewBox="0 0 10 10"><path d="M0,2 H10 V8 H0Z M0,2 L5,6 L10,2" fill="none" stroke="var(--ink)"/></svg>fowler@tamselbriargifts.example</li>
        <li><svg viewBox="0 0 10 10"><circle cx="5" cy="5" r="4.5"/></svg>www.tamselbriargifts.example</li>
      </ul>
    </div>
    <p class="caption">Front Card Option_06</p>
  </section>

</main>
</body>
</html>
```